RTamberly Business Cards & Letterhead

I have a logo but need a design for some new business cards. We are a Design-Build Firm that specializes in the design and construction of commercial projects.
the cards need to be professional. no cartoon stuff.
i would like to have the cards in AI format so I can update the card as needed. Logo is provided.
Our Address is: 4183 Marwood Ln. Larkton, Ohio 27614

```html
<!DOCTYPE html>
<html lang="en">
<head>
<meta charset="utf-8">
<title>RTamberly Business Card</title>
<link rel="stylesheet" href="https://fonts.googleapis.com/css2?family=Open+Sans:wght@400;700&display=swap">
<style>
  :root {
    --backdrop: #8a8b8e;
    --card-white: #ffffff;
    --card-dark: #54565b;
    --ink-dark: #3c3e43;
    --ink-body: #4a4a4a;
    --brand-blue: #0a72b9;
    --brand-blue-deep: #0b4a86;
    --brand-blue-bright: #1a86cf;
  }
  * { box-sizing: border-box; margin: 0; padding: 0; }
  html, body { width: 1200px; height: 781px; overflow: hidden; }
  body {
    background: var(--backdrop);
    font-family: "Open Sans", Arial, sans-serif;
    position: relative;
  }
  .card {
    position: absolute;
    top: 239px;
    width: 530px;
    height: 303px;
    border-radius: 22px;
    overflow: hidden;
  }
  .card--front { left: 40px; background: var(--card-white); }
  .card--back { left: 630px; background: var(--card-dark); }

  .wordmark {
    font-weight: 700;
    line-height: 1;
    white-space: nowrap;
  }
  .card--front .wordmark {
    position: absolute;
    left: 30px;
    top: 32px;
    font-size: 32px;
    color: var(--ink-dark);
  }
  .contact {
    position: absolute;
    left: 30px;
    top: 96px;
    width: 250px;
    font-size: 13px;
    line-height: 19px;
    color: var(--ink-body);
  }
  .contact__name {
    font-size: 20px;
    line-height: 24px;
    font-weight: 700;
    color: var(--brand-blue);
    text-transform: uppercase;
    letter-spacing: 0.3px;
  }
  .contact__title { margin-bottom: 2px; }
  .brand-panel {
    position: absolute;
    right: 34px;
    bottom: 28px;
    width: 220px;
    height: 160px;
  }
  .card--back .wordmark {
    position: absolute;
    left: 0;
    right: 0;
    top: 50%;
    transform: translateY(-50%);
    text-align: center;
    font-size: 44px;
    color: var(--card-white);
  }
</style>
</head>
<body>
  <section class="card card--front">
    <div class="wordmark">RTamberly</div>
    <div class="contact">
      <p class="contact__name">Morgan Tamberly</p>
      <p class="contact__title">President</p>
      <p>4183 Marwood Ln. Larkton,</p>
      <p>Ohio 27614</p>
      <p>614-555-0148</p>
      <p>Projects@RTamberly.com</p>
      <p>www.RTamberly.com</p>
    </div>
    <svg class="brand-panel" viewBox="0 0 220 160" role="img" aria-label="Large blue brand decoration">
      <defs>
        <linearGradient id="panelBlue" x1="0" y1="1" x2="1" y2="0">
          <stop offset="0" stop-color="#0b4a86"/>
          <stop offset="1" stop-color="#1a86cf"/>
        </linearGradient>
      </defs>
      <rect x="0" y="0" width="220" height="160" rx="24" fill="url(#panelBlue)"/>
    </svg>
  </section>

  <section class="card card--back">
    <div class="wordmark">RTamberly</div>
  </section>
</body>
</html>
```